Need a design for Office wall, Pull up banner and brochure.

Hi there, We are looking for a design for our Mission, Vision and Values. We need it for our wall design, our pull up banner, and for our brochure. Full instructions have been provided in the Instructions png file submitted. Please let me know.

Our brand colours are:

Brand colours:
#0070BA
#000A3F
#6D6E71

Font styles to use
Other font styles liked:
• FF Meta Georgian Book

Colors

Designer to choose colors to be used in the design.

```html
<!DOCTYPE html>
<html lang="en">
<head>
<meta charset="utf-8">
<title>Ashcombe Reid – Vision, Mission, Value</title>
<link rel="stylesheet" href="https://fonts.googleapis.com/css2?family=Fira+Sans:wght@400;500&display=swap">
<style>
  :root {
    --brand-blue: #0070BA;
    --brand-navy: #000A3F;
    --brand-grey: #6D6E71;
    --value-violet: #6C6EF0;
    --logo-slate: #3F4466;
    --body-ink: #0B0C2E;
    --bg-light: #FAFAFA;
    --bg-edge: #E6E6E8;
  }
  html, body {
    margin: 0;
    padding: 0;
    overflow: hidden;
  }
  body {
    width: 700px;
    height: 1200px;
  }
  .banner {
    position: relative;
    width: 700px;
    height: 1200px;
    overflow: hidden;
    background: radial-gradient(ellipse 75% 60% at 45% 50%, #FFFFFF 0%, var(--bg-light) 55%, var(--bg-edge) 100%);
    font-family: "Fira Sans", sans-serif;
  }
  .shapes {
    position: absolute;
    inset: 0;
    width: 700px;
    height: 1200px;
  }
  .brand {
    position: absolute;
    left: 58px;
    top: 70px;
    color: var(--logo-slate);
  }
  .brand-name {
    display: flex;
    align-items: center;
    gap: 10px;
    font-size: 28px;
    font-weight: 400;
    letter-spacing: 1.5px;
    line-height: 1;
    color: var(--logo-slate);
  }
  .brand-dot {
    width: 16px;
    height: 16px;
    border-radius: 50%;
    background: var(--brand-blue);
  }
  .brand-tagline {
    margin: 8px 0 0 38px;
    font-size: 15.5px;
    letter-spacing: 0.8px;
    color: #808085;
  }
  .brand-incorporating {
    margin: 8px 0 0 95px;
    font-size: 10.5px;
    letter-spacing: 1.3px;
    text-transform: uppercase;
    color: var(--logo-slate);
  }
  .statement {
    position: absolute;
  }
  .statement-title {
    margin: 0 0 4px;
    font-size: 33px;
    font-weight: 500;
    line-height: 1.1;
    letter-spacing: 0.5px;
  }
  .statement-text {
    margin: 0;
    font-size: 16px;
    line-height: 21.5px;
    letter-spacing: 0.3px;
    color: var(--body-ink);
  }
  .statement--vision { left: 314px; top: 302px; }
  .statement--vision .statement-title { color: var(--brand-blue); word-spacing: 6px; }
  .statement--mission { left: 398px; top: 597px; }
  .statement--mission .statement-title { color: var(--brand-navy); }
  .statement--value { left: 286px; top: 962px; }
  .statement--value .statement-title { color: var(--value-violet); }
</style>
</head>
<body>
<main class="banner">
  <svg class="shapes" viewBox="0 0 1470 2520" aria-hidden="true">
    <defs>
      <filter id="glow-soft" x="-30%" y="-30%" width="160%" height="160%">
        <feGaussianBlur stdDeviation="28"/>
      </filter>
      <linearGradient id="disc-fill" x1="0" y1="0" x2="0" y2="1">
        <stop offset="0" stop-color="#FFFFFF"/>
        <stop offset="0.5" stop-color="#F7F7F7"/>
        <stop offset="1" stop-color="#C9C9CB"/>
      </linearGradient>
    </defs>

    <!-- centre hub -->
    <g class="hub">
      <path d="M12,1283 A160,160 0 0 1 145,1366" fill="none" stroke="var(--brand-blue)" stroke-width="11"/>
      <path d="M145,1366 A160,160 0 0 1 145,1520" fill="none" stroke="var(--brand-navy)" stroke-width="11"/>
      <path d="M145,1520 A160,160 0 0 1 12,1603" fill="none" stroke="var(--value-violet)" stroke-width="11"/>
      <circle cx="0" cy="1443" r="150" fill="#D8D8DA"/>
      <circle cx="0" cy="1443" r="138" fill="url(#disc-fill)"/>
    </g>

    <!-- vision petal -->
    <g class="petal petal--vision">
      <path d="M42,840 Q42,755 130,762 Q360,795 545,995 Q580,1050 525,1113 L375,1200 Q325,1225 282,1188 Q200,1105 100,1083 Q42,1068 42,1010 Z" fill="#3FA9E8" filter="url(#glow-soft)" transform="translate(0,-18)"/>
      <path d="M42,840 Q42,755 130,762 Q360,795 545,995 Q580,1050 525,1113 L375,1200 Q325,1225 282,1188 Q200,1105 100,1083 Q42,1068 42,1010 Z" fill="var(--brand-blue)"/>
      <circle cx="287" cy="981" r="90" fill="none" stroke="#FFFFFF" stroke-width="14"/>
      <circle cx="287" cy="981" r="62" fill="#FFFFFF"/>
      <circle cx="322" cy="928" r="45" fill="var(--brand-blue)"/>
    </g>

    <!-- value petal -->
    <g class="petal petal--value">
      <path d="M42,2046 Q42,2131 130,2124 Q360,2091 545,1891 Q580,1836 525,1773 L375,1686 Q325,1661 282,1698 Q200,1781 100,1803 Q42,1818 42,1876 Z" fill="#8F8FFF" filter="url(#glow-soft)" transform="translate(0,18)"/>
      <path d="M42,2046 Q42,2131 130,2124 Q360,2091 545,1891 Q580,1836 525,1773 L375,1686 Q325,1661 282,1698 Q200,1781 100,1803 Q42,1818 42,1876 Z" fill="var(--value-violet)"/>
      <path d="M280,1795 L309,1858 L376,1866 L327,1913 L340,1979 L280,1946 L220,1979 L233,1913 L184,1866 L251,1858 Z" fill="none" stroke="#FFFFFF" stroke-width="13" stroke-linejoin="round"/>
      <path d="M280,1852 L293,1880 L322,1884 L300,1904 L306,1933 L280,1918 L254,1933 L260,1904 L238,1884 L267,1880 Z" fill="#FFFFFF"/>
    </g>

    <!-- mission petal -->
    <g class="petal petal--mission">
      <path d="M400,1250 L555,1162 Q635,1125 665,1205 Q705,1320 705,1443 Q705,1566 665,1681 Q635,1761 555,1724 L400,1636 Q355,1605 370,1555 Q383,1500 383,1443 Q383,1386 370,1331 Q355,1281 400,1250 Z" fill="#1A2060" filter="url(#glow-soft)" transform="translate(22,0)"/>
      <path d="M400,1250 L555,1162 Q635,1125 665,1205 Q705,1320 705,1443 Q705,1566 665,1681 Q635,1761 555,1724 L400,1636 Q355,1605 370,1555 Q383,1500 383,1443 Q383,1386 370,1331 Q355,1281 400,1250 Z" fill="var(--brand-navy)"/>
      <path d="M563,1365 A90,90 0 1 0 615,1417" fill="none" stroke="#FFFFFF" stroke-width="14"/>
      <path d="M540,1403 A46,46 0 1 0 577,1438" fill="none" stroke="#FFFFFF" stroke-width="14"/>
      <path d="M536,1446 L606,1376" stroke="#FFFFFF" stroke-width="14" stroke-linecap="round"/>
      <path d="M590,1374 L613,1349 L622,1368 L637,1374 L610,1401 L594,1396 Z" fill="#FFFFFF"/>
    </g>
  </svg>

  <header class="brand">
    <div class="brand-name"><span class="brand-dot"></span>Ashcombe Reid</div>
    <div class="brand-tagline">Accountants &amp; Business Advisors</div>
    <div class="brand-incorporating">Incorporating Peter M Dalton</div>
  </header>

  <section class="statement statement--vision">
    <h2 class="statement-title">OUR VISION</h2>
    <p class="statement-text">Lorem ipsum dolor sit amet.<br>Dolores sit lorem. Eirmod<br>feugait dolore facilisi<br>imperdiet et justo. Sit dolore<br>sed dolor. Vulputate aliquyam</p>
  </section>

  <section class="statement statement--mission">
    <h2 class="statement-title">OUR MISSION</h2>
    <p class="statement-text">Lorem ipsum dolor sit amet.<br>Dolores sit lorem. Eirmod<br>feugait dolore facilisi<br>imperdiet et justo. Sit dolore<br>sed dolor. Vulputate aliquyam<br>iriure dolor duo kasd est. Sit<br>molestie vulputate. Ea eirmod</p>
  </section>

  <section class="statement statement--value">
    <h2 class="statement-title">OUR VALUE</h2>
    <p class="statement-text">Lorem ipsum dolor sit amet.<br>Dolores sit lorem. Eirmod<br>feugait dolore facilisi<br>imperdiet et justo. Sit dolore<br>sed dolor. Vulputate aliquyam</p>
  </section>
</main>
</body>
</html>
```